PLOVA Business Card

Crestline Property Upgrades and Refits. I need a business card designed for this new high end renovation business. I would like the logo centered on the back side with the ABN (71 903 257 146) on the bottom right hand corner.

I would like the following information placed on the other side along with some customized pattern or design.

Patrick Delvane
Director
Phone: 1300 847 926
Fax: (02) 9415 6702
Website: www.plovabuilding.com.au
Email: p.delvane@plovabuilding.com.au
PO Box 87,
Kelwyn NSW 2091

(FB Logo) PLOVA - Crestline Property Upgrades and Refits

The final design should communicate professionalism and trust.

Back side background colour: white
Front side: Undecided

```html
<!DOCTYPE html>
<html lang="en">
<head>
<meta charset="UTF-8">
<title>PLOVA Business Card</title>
<link href="https://fonts.googleapis.com/css2?family=Cinzel:wght@400;700&family=Open+Sans:wght@400;600;700&display=swap" rel="stylesheet">
<style>
  :root {
    --navy: #1c1c5e;
    --blue: #1f5aa6;
    --ink: #2a2a2a;
    --paper: #ffffff;
    --backdrop: #e6e7ea;
    --rule: #333333;
  }
  * { box-sizing: border-box; margin: 0; padding: 0; }
  html, body { width: 1200px; height: 1000px; overflow: hidden; }
  body {
    background: var(--backdrop);
    font-family: "Open Sans", Arial, sans-serif;
    position: relative;
  }
  .card {
    position: absolute;
    left: 250px;
    width: 700px;
    height: 400px;
    background: var(--paper);
    box-shadow: 0 6px 20px rgba(0,0,0,0.18);
    overflow: hidden;
  }
  .card--front { top: 60px; }
  .card--back { top: 540px; }

  /* Front */
  .front-band {
    position: absolute; left: 0; top: 0; width: 100%; height: 118px;
    background: var(--navy);
    display: flex; align-items: center; justify-content: center;
  }
  .brand { text-align: center; }
  .brand-name {
    font-family: "Cinzel", Georgia, serif; font-weight: 700;
    font-size: 46px; letter-spacing: 4px; line-height: 1;
  }
  .brand-tagline {
    display: flex; align-items: center; gap: 10px; margin-top: 6px;
    font-family: "Cinzel", Georgia, serif; font-size: 12px; letter-spacing: 1px;
  }
  .brand-tagline::before, .brand-tagline::after {
    content: ""; width: 40px; height: 1px; background: currentColor;
  }
  .front-band .brand-name, .front-band .brand-tagline { color: #ffffff; }

  .holder {
    position: absolute; left: 0; right: 0; top: 146px; text-align: center;
  }
  .holder-name {
    color: var(--blue); font-weight: 700; font-size: 22px; letter-spacing: 1px;
    text-transform: uppercase;
  }
  .holder-role { color: var(--ink); font-weight: 700; font-size: 15px; margin-top: 2px; }

  .contact-rule {
    position: absolute; left: 190px; width: 320px; top: 222px;
    height: 1.5px; background: var(--rule);
  }
  .contact-list {
    position: absolute; left: 215px; top: 236px; list-style: none;
    color: var(--ink); font-size: 15px; line-height: 22px;
  }
  .contact-list li { display: flex; align-items: center; gap: 10px; }
  .contact-list .indent { padding-left: 30px; }
  .icon { width: 20px; height: 20px; flex: none; }

  .website {
    position: absolute; left: 0; right: 0; bottom: 22px; text-align: center;
    color: var(--navy); font-size: 15px; letter-spacing: 2.5px;
  }
  .tick-mark {
    position: absolute; bottom: 32px; width: 22px; height: 3px; background: var(--navy);
  }
  .tick-mark--left { left: 30px; }
  .tick-mark--right { right: 30px; }

  /* Back */
  .back-brand {
    position: absolute; left: 0; right: 0; top: 110px;
    display: flex; justify-content: center;
  }
  .back-brand .brand-name { color: var(--navy); font-size: 64px; }
  .back-brand .brand-tagline { color: var(--blue); font-size: 14px; margin-top: 8px; }
  .back-stripes { position: absolute; left: 0; bottom: 0; width: 700px; height: 90px; }
  .abn {
    position: absolute; right: 40px; bottom: 16px; line-height: 20px;
    color: #ffffff; font-family: "Cinzel", Georgia, serif; font-size: 15px; letter-spacing: 1px;
  }
</style>
</head>
<body>

<section class="card card--front" aria-label="Business card front">
  <div class="front-band">
    <div class="brand">
      <div class="brand-name">PLOVA</div>
      <div class="brand-tagline">Crestline Property Upgrades &amp; Refits</div>
    </div>
  </div>

  <div class="holder">
    <div class="holder-name">Patrick Delvane</div>
    <div class="holder-role">Director</div>
  </div>

  <div class="contact-rule"></div>

  <ul class="contact-list">
    <li>
      <svg class="icon" viewBox="0 0 20 20" aria-hidden="true"><rect width="20" height="20" rx="3" fill="#1f5aa6"/><path d="M6 4.5c1 0 1.8 2.2 1.2 3l-.7.8c.7 1.6 2 2.9 3.6 3.6l.8-.7c.8-.6 3 .2 3 1.2v1.5c0 .8-1 1.6-2.3 1.3C8 14.4 5.6 12 4.8 8.3 4.5 7 5.3 4.5 6 4.5z" fill="#fff"/></svg>
      1300 847 926
    </li>
    <li>
      <svg class="icon" viewBox="0 0 20 20" aria-hidden="true"><rect width="20" height="20" rx="3" fill="#1f5aa6"/><rect x="5" y="8" width="10" height="7" rx="1" fill="#fff"/><rect x="7" y="4" width="6" height="4" fill="#fff"/><rect x="7" y="10" width="6" height="1.2" fill="#1f5aa6"/></svg>
      (02) 9415 6702
    </li>
    <li>
      <svg class="icon" viewBox="0 0 20 20" aria-hidden="true"><rect width="20" height="20" rx="3" fill="#1f5aa6"/><rect x="4" y="6" width="12" height="8" fill="#fff"/><path d="M4 6l6 5 6-5" fill="none" stroke="#1f5aa6" stroke-width="1.2"/></svg>
      p.delvane@plovabuilding.com.au
    </li>
    <li>
      <svg class="icon" viewBox="0 0 20 20" aria-hidden="true"><rect width="20" height="20" rx="3" fill="#1f5aa6"/><path d="M10 3.5c2.6 0 4.5 1.9 4.5 4.3 0 3.2-4.5 8.2-4.5 8.2S5.5 11 5.5 7.8C5.5 5.4 7.4 3.5 10 3.5z" fill="#fff"/><circle cx="10" cy="7.8" r="1.6" fill="#1f5aa6"/></svg>
      PO Box 87,
    </li>
    <li class="indent">Kelwyn NSW 2091</li>
  </ul>

  <span class="tick-mark tick-mark--left"></span>
  <span class="tick-mark tick-mark--right"></span>
  <div class="website">www.plovabuilding.com.au</div>
</section>

<section class="card card--back" aria-label="Business card back">
  <div class="back-brand">
    <div class="brand">
      <div class="brand-name">PLOVA</div>
      <div class="brand-tagline">Crestline Property Upgrades &amp; Refits</div>
    </div>
  </div>

  <svg class="back-stripes" viewBox="0 0 700 90" aria-hidden="true">
    <polygon points="0,42 414,42 436,20 700,20 700,26 438.5,26 416.5,48 0,48" fill="#1c1c5e"/>
    <polygon points="0,56 420,56 442,34 700,34 700,90 0,90" fill="#1c1c5e"/>
  </svg>
  <div class="abn">ABN 71 903 257 146</div>
</section>

</body>
</html>
```